Lone Willow Estate Vault Reserve Wine Label (Front and Back)

I need to create an elite tier wine label.  I would like it to be in a light, natural color with silver or gold.  I would like it to look rich and expensive, mostly monochromatic, elegantly simple.  It will need to stand up next to wine labels that are black and charcoal colored and look like the more expensive wine of the 3.  I have attached a similar label that it will be grouped with and some instructions.
We are a winery in southeast Washington state with a reputation for fine wines and top notch terroir.  We want to present family, tradition and high value wine in the bottle.

```html
<!DOCTYPE html>
<html lang="en">
<head>
<meta charset="utf-8">
<title>Lone Willow Estate – Vault Reserve Label Options</title>
<link href="https://fonts.googleapis.com/css2?family=Cinzel:wght@400;500&family=Cormorant+Garamond:wght@500&family=Open+Sans:wght@400&display=swap" rel="stylesheet">
<style>
  :root {
    --bg-top: #a9a9ab;
    --bg-bottom: #e4e4e6;
    --heading: #555557;
    --label-ivory: #f3eee3;
    --label-linen: #e3dacb;
    --ink: #4a4238;
    --gold: #b8943a;
    --gold-deep: #9c7a22;
    --gold-light: #ecd47a;
    --band-text: #5e4814;
  }
  * { box-sizing: border-box; margin: 0; padding: 0; }
  html, body { width: 1200px; height: 900px; overflow: hidden; }
  body {
    background: linear-gradient(180deg, var(--bg-top) 0%, #c3c3c5 60%, var(--bg-bottom) 100%);
    font-family: "Cinzel", serif;
    position: relative;
  }
  .option-heading {
    position: absolute;
    top: 42px;
    width: 310px;
    text-align: center;
    font-family: "Open Sans", sans-serif;
    font-weight: 400;
    font-size: 30px;
    letter-spacing: 1px;
    color: var(--heading);
  }
  .option-heading--one { left: 245px; }
  .option-heading--two { left: 645px; }

  .label {
    position: absolute;
    width: 310px;
    border-radius: 3px;
    color: var(--ink);
    text-align: center;
    box-shadow: 0 2px 10px rgba(0, 0, 0, 0.12);
  }
  .label--one {
    left: 245px;
    top: 180px;
    height: 535px;
    background: var(--label-ivory);
  }
  .label--two {
    left: 645px;
    top: 130px;
    height: 585px;
    background: linear-gradient(180deg, var(--label-ivory) 0%, var(--label-ivory) 265px, var(--label-linen) 265px, var(--label-linen) 100%);
  }
  .label > * { position: absolute; left: 0; right: 0; }

  .seal {
    top: -50px;
    left: 59px;
    right: auto;
    width: 192px;
    height: 192px;
  }
  .seal svg { display: block; }
  .seal-name {
    position: absolute;
    inset: 0;
    display: flex;
    align-items: center;
    justify-content: center;
    font-family: "Cinzel", serif;
    font-weight: 500;
    font-size: 21px;
    line-height: 1.2;
    color: var(--ink);
  }
  .winery-name {
    font-family: "Cinzel", serif;
    font-weight: 400;
    font-size: 30px;
    line-height: 34px;
    color: var(--gold-deep);
  }
  .estate-line { font-size: 15px; line-height: 20px; letter-spacing: 1.5px; }
  .region { font-size: 20px; line-height: 26px; letter-spacing: 2.5px; }
  .tier-block { left: 40px; right: 40px; }
  .tier-rule { display: block; width: 100%; height: 10px; }
  .tier-name {
    font-size: 23px;
    line-height: 28px;
    letter-spacing: 1.5px;
    padding: 5px 0;
    color: var(--ink);
  }
  .vintage { font-size: 16px; line-height: 20px; letter-spacing: 2px; }
  .varietal { font-size: 15px; line-height: 20px; letter-spacing: 1.5px; }
  .heritage-band {
    left: 4px;
    right: 4px;
    bottom: 4px;
    height: 40px;
    display: flex;
    align-items: center;
    justify-content: center;
    background: linear-gradient(90deg, var(--gold-deep) 0%, var(--gold-light) 45%, #c9a94a 75%, var(--gold-deep) 100%);
    font-family: "Cormorant Garamond", serif;
    font-weight: 500;
    font-size: 10.5px;
    letter-spacing: 0.4px;
    color: var(--band-text);
    text-transform: uppercase;
  }
  .wordmark-frame {
    left: 80px;
    right: auto;
    width: 150px;
    height: 160px;
    border: 4px solid var(--gold);
    display: flex;
    align-items: center;
    justify-content: center;
    font-size: 22px;
    line-height: 1.25;
    color: var(--gold-deep);
  }

  .label--one .winery-name { top: 162px; }
  .label--one .estate-line { top: 243px; }
  .label--one .region { top: 303px; }
  .label--one .tier-block { top: 360px; }
  .label--one .vintage { top: 430px; }
  .label--one .varietal { top: 462px; }

  .label--two .winery-name { top: 45px; }
  .label--two .region { top: 128px; }
  .label--two .wordmark-frame { top: 188px; }
  .label--two .estate-line { top: 368px; }
  .label--two .tier-block { top: 392px; }
  .label--two .vintage { top: 467px; }
  .label--two .varietal { top: 502px; }
</style>
</head>
<body>
  <svg width="0" height="0" style="position:absolute" aria-hidden="true">
    <defs>
      <linearGradient id="gold-fill" x1="0" y1="0" x2="1" y2="1">
        <stop offset="0" stop-color="#f0d97e"/>
        <stop offset="0.5" stop-color="#c9a94a"/>
        <stop offset="1" stop-color="#8f6e1c"/>
      </linearGradient>
      <symbol id="tier-rule" viewBox="0 0 230 10">
        <line x1="0" y1="5" x2="230" y2="5" stroke="#b8943a" stroke-width="2"/>
        <rect x="111" y="1" width="8" height="8" transform="rotate(45 115 5)" fill="#b8943a"/>
      </symbol>
    </defs>
  </svg>

  <h2 class="option-heading option-heading--one">OPTION 1</h2>
  <h2 class="option-heading option-heading--two">OPTION 2</h2>

  <div class="label label--one">
    <div class="seal">
      <svg width="192" height="192" viewBox="0 0 192 192" aria-hidden="true">
        <circle cx="96" cy="96" r="95" fill="url(#gold-fill)"/>
      </svg>
      <div class="seal-name">Lone<br>Willow<br>Estate</div>
    </div>
    <h1 class="winery-name">Lone Willow<br>Estate</h1>
    <p class="estate-line">Estate Vineyard</p>
    <p class="region">Horse Heaven Hills</p>
    <div class="tier-block">
      <svg class="tier-rule" viewBox="0 0 230 10" preserveAspectRatio="none"><use href="#tier-rule"/></svg>
      <p class="tier-name">Vault Reserve</p>
      <svg class="tier-rule" viewBox="0 0 230 10" preserveAspectRatio="none"><use href="#tier-rule"/></svg>
    </div>
    <p class="vintage">2022</p>
    <p class="varietal">Cabernet Sauvignon</p>
    <p class="heritage-band">Family stewards of the land for 5 generations</p>
  </div>

  <div class="label label--two">
    <h1 class="winery-name">Lone Willow<br>Estate</h1>
    <p class="region">Horse Heaven Hills</p>
    <div class="wordmark-frame">Lone<br>Willow<br>Estate</div>
    <p class="estate-line">Estate Vineyard</p>
    <div class="tier-block">
      <svg class="tier-rule" viewBox="0 0 230 10" preserveAspectRatio="none"><use href="#tier-rule"/></svg>
      <p class="tier-name">Vault Reserve</p>
      <svg class="tier-rule" viewBox="0 0 230 10" preserveAspectRatio="none"><use href="#tier-rule"/></svg>
    </div>
    <p class="vintage">2022</p>
    <p class="varietal">Cabernet Sauvignon</p>
    <p class="heritage-band">Family stewards of the land for 5 generations</p>
  </div>
</body>
</html>
```